Upmarket Artwork, Furniture Retailer needs to Improve existing Vendlo Product Template Page

We need to improve an existing design for a Vendlo product page. For professional quality we will then like to use the same designer for further work e.g vendlo store(Web page)
We need a Web Designer for an exciting new online retailer based in Sydney. Our product is upmarket Scandanavian designed indoor furniture and Rattan outdoor furniture and Modernist Artwork.
Existing Banners,Logo, text, and template can be the same but the Graphic Design need improvement to give the Vendlo product page an edge. We like the Green and Brown colours. Attached is teh logo and the extsing Product template

Reason: Thank you everyone for sending through your designs. Soem designs have come in late today and we need some extra time to contact designers. We will be in contact with you to let you know how you went. Kind Regards Melinda

Reason: Still waiting on some redesigns. My apologies for the belated reply. Thank you everyone for sending through great quality work.

Reason: My apologies for the delay. We are waiting on a re design to finalise. Thank you everyone for your patience. Cheers Melinda

Target Market(s)

Upmarket house proud 25-55 professionals

Industry/Entity Type

Graphic Design

Requirements
Must have
• To have an edge to Maximise Buyers
Nice to have
• To use the colours Greens and browns

```html
<!DOCTYPE html>
<html lang="en">
<head>
<meta charset="utf-8">
<title>Lumera – Product Page</title>
<link rel="stylesheet" href="https://fonts.googleapis.com/css2?family=Comfortaa:wght@400&family=Lora:ital,wght@1,400;1,700&family=Oswald:wght@500&family=Roboto+Condensed:wght@700&display=swap">
<style>
:root{
  --bg-top:#7d6433;
  --bg-bottom:#745c2e;
  --panel:#3d301d;
  --panel-inner:#46381f;
  --panel-edge:#5b4a2c;
  --frame:#4a3b22;
  --green:#4f8d28;
  --green-dark:#356618;
  --green-light:#83b63f;
  --cream:#f1ead6;
  --text-soft:#e6dcc2;
  --line:#a48c5a;
}
*{box-sizing:border-box;margin:0;padding:0}
html,body{width:1200px;height:4915px;overflow:hidden}
body{background:linear-gradient(180deg,var(--bg-top),var(--bg-bottom));position:relative;font-family:"Lora",Georgia,serif;color:var(--cream)}
.abs{position:absolute}

/* Header */
.brand{left:0;top:50px;width:1200px;text-align:center}
.brand-mark{width:34px;height:34px;border-radius:50%;background:var(--green-light);margin:0 auto 18px}
.brand-name{font-family:"Comfortaa",sans-serif;font-size:84px;line-height:1;color:var(--cream);letter-spacing:2px}
.main-nav{left:0;top:315px;width:1200px;height:62px;border-top:1px solid var(--line);border-bottom:1px solid var(--line);display:flex;justify-content:center;align-items:center;gap:46px;font-style:italic;font-size:18px}

/* Hero */
.hero{left:20px;top:410px;width:1160px;height:750px;background:var(--frame);border-radius:10px;box-shadow:0 6px 14px rgba(0,0,0,.45);padding:28px}
.hero-art{width:100%;height:100%;background:linear-gradient(135deg,#c9a237 0%,#e9dfc0 35%,#d8cfb5 55%,#6a5a3a 75%,#e9e2cc 100%)}
.hero-badge{right:58px;bottom:40px;width:180px;height:180px;border-radius:50%;background:var(--green);border:8px solid #fff}

/* Ribbons */
.band{left:0;width:1200px;height:68px;background:var(--green);display:flex;align-items:center;justify-content:center;font-family:"Roboto Condensed",sans-serif;font-weight:700;color:#fff;box-shadow:0 4px 8px rgba(0,0,0,.35)}
.product-title{top:1188px;font-size:25px}
.product-title .price{font-size:34px;margin-left:10px}
.featured-title{top:4374px;font-size:30px}

/* Info panels */
.info-panel{width:557px;height:410px;background:var(--panel);border:6px solid var(--panel-edge);border-radius:6px;box-shadow:0 5px 12px rgba(0,0,0,.4)}
.info-panel h2{font-family:"Oswald",sans-serif;font-weight:500;font-size:32px;color:var(--green-light);padding:24px 30px 14px;background:var(--panel-inner)}
.panel-text{padding:18px 30px;font-style:italic;font-weight:700;font-size:14.5px;line-height:36px;color:var(--text-soft)}

/* Thumbnails */
.thumb{width:250px;height:392px;background:var(--frame);padding:12px;border-radius:4px;box-shadow:0 6px 12px rgba(0,0,0,.5)}
.thumb-art{width:100%;height:100%;background:linear-gradient(160deg,#2a2316 0%,#8b7a52 28%,#e4dac0 45%,#c9a237 70%,#e8dfc4 100%)}
.thumb.featured{overflow:hidden}
.thumb-ribbon{top:34px;left:-34px;width:160px;height:34px;background:var(--green);transform:rotate(-45deg);display:flex;align-items:center;justify-content:center;font-family:"Roboto Condensed",sans-serif;font-weight:700;font-size:13px;color:#fff;box-shadow:0 2px 4px rgba(0,0,0,.35)}

/* Service panels */
.service-panel{width:460px;height:573px;background:var(--panel);border:6px solid var(--panel-edge);border-radius:4px;box-shadow:0 5px 12px rgba(0,0,0,.4)}
.service-heading{top:-14px;left:-36px;width:520px;height:62px;background:var(--green);display:flex;align-items:center;justify-content:center;font-family:"Roboto Condensed",sans-serif;font-weight:700;font-size:30px;color:#fff;box-shadow:0 4px 6px rgba(0,0,0,.35)}
.service-panel .panel-text{padding:78px 40px 0;line-height:38px}
</style>
</head>
<body>

<header class="brand abs">
  <div class="brand-mark"></div>
  <div class="brand-name">Lumera</div>
</header>

<nav class="main-nav abs">
  <span>Payment</span><span>Delivery</span><span>Warranty</span><span>About us</span><span>Contact us</span><span>Vendlo Store</span>
</nav>

<section class="hero abs">
  <div class="hero-art" role="img" aria-label="Abstract oil painting with metal elements in gold, cream and dark brown tones"></div>
  <div class="hero-badge abs"></div>
</section>

<div class="band product-title abs">Modern Oil Painting- Metal Elements to evoke Beautiful Landscapem Canvas-Framed<span class="price">RRP $193</span></div>

<section class="info-panel abs" style="left:41px;top:1290px">
  <h2>Description</h2>
  <p class="panel-text">Lorem ipsum dolor sit amet, consectetur adipiscing elit. Proin tempus dolor vitae purus tincidunt nec iaculis ipsum mollis. Lorem ipsum dolor sit amet, consectetur adipiscing elit. Proin tempus dolor vitae purus tincidunt nec iaculis ipsum mollieret gravida est. Vivamus in magna eget erat iaculis iaculis. Cras</p>
</section>
<section class="info-panel abs" style="left:612px;top:1290px">
  <h2>Quality Features</h2>
  <p class="panel-text">Lorem ipsum dolor sit amet, consectetur adipiscing elit. Proin tempus dolor vitae purus tincidunt nec iaculis ipsum mollis. Lorem ipsum dolor sit amet, consectetur adipiscing elit. Proin tempus dolor vitae purus tincidunt nec iaculis ipsum mollieret gravida est. Vivamus in magna eget erat iaculis iaculis. Cras</p>
</section>
<section class="info-panel abs" style="left:41px;top:1740px">
  <h2>Package Includes</h2>
  <p class="panel-text">Lorem ipsum dolor sit amet, consectetur adipiscing elit. Proin tempus dolor vitae purus tincidunt nec iaculis ipsum mollis. Lorem ipsum dolor sit amet, consectetur adipiscing elit. Proin tempus dolor vitae purus tincidunt nec iaculis ipsum mollieret gravida est. Vivamus in magna eget erat iaculis iaculis. Cras</p>
</section>
<section class="info-panel abs" style="left:612px;top:1740px">
  <h2>Dimensions</h2>
  <p class="panel-text">Lorem ipsum dolor sit amet, consectetur adipiscing elit. Proin tempus dolor vitae purus tincidunt nec iaculis ipsum mollis. Lorem ipsum dolor sit amet, consectetur adipiscing elit. Proin tempus dolor vitae purus tincidunt nec iaculis ipsum mollieret gravida est. Vivamus in magna eget erat iaculis iaculis. Cras</p>
</section>

<div class="thumb abs" style="left:41px;top:2232px"><div class="thumb-art" role="img" aria-label="Product view of the painting"></div></div>
<div class="thumb abs" style="left:328px;top:2232px"><div class="thumb-art" role="img" aria-label="Product view of the painting"></div></div>
<div class="thumb abs" style="left:615px;top:2232px"><div class="thumb-art" role="img" aria-label="Product view of the painting"></div></div>
<div class="thumb abs" style="left:902px;top:2232px"><div class="thumb-art" role="img" aria-label="Product view of the painting"></div></div>
<div class="thumb abs" style="left:41px;top:2672px"><div class="thumb-art" role="img" aria-label="Product view of the painting"></div></div>
<div class="thumb abs" style="left:328px;top:2672px"><div class="thumb-art" role="img" aria-label="Product view of the painting"></div></div>
<div class="thumb abs" style="left:615px;top:2672px"><div class="thumb-art" role="img" aria-label="Product view of the painting"></div></div>
<div class="thumb abs" style="left:902px;top:2672px"><div class="thumb-art" role="img" aria-label="Product view of the painting"></div></div>

<section class="service-panel abs" style="left:90px;top:3170px">
  <h2 class="service-heading abs">Warranty</h2>
  <p class="panel-text">Lorem ipsum dolor sit amet, consectetur adipiscing elit. Proin tempus dolor vitae purus tincidunt nec iaculis ipsum mollis. Lorem ipsum dolor sit amet, consectetur adipiscing elit. Proin tempus dolor vitae purus tincidunt nec iaculis ipsum mollieret gravida est. Vivamus in magna eget erat iaculis iaculis. Cras lacinia, justo ac pellentesque placerat, nunc tortor commodo justo, non cursus leo sem nec metus. Quisque</p>
</section>
<section class="service-panel abs" style="left:650px;top:3170px">
  <h2 class="service-heading abs">Payment</h2>
  <p class="panel-text">Lorem ipsum dolor sit amet, consectetur adipiscing elit. Proin tempus dolor vitae purus tincidunt nec iaculis ipsum mollis. Lorem ipsum dolor sit amet, consectetur adipiscing elit. Proin tempus dolor vitae purus tincidunt nec iaculis ipsum mollieret gravida est. Vivamus in magna eget erat iaculis iaculis. Cras lacinia, justo ac pellentesque placerat, nunc tortor commodo justo, non cursus leo sem nec metus. Quisque</p>
</section>
<section class="service-panel abs" style="left:90px;top:3800px">
  <h2 class="service-heading abs">Delivery</h2>
  <p class="panel-text">Lorem ipsum dolor sit amet, consectetur adipiscing elit. Proin tempus dolor vitae purus tincidunt nec iaculis ipsum mollis. Lorem ipsum dolor sit amet, consectetur adipiscing elit. Proin tempus dolor vitae purus tincidunt nec iaculis ipsum mollieret gravida est. Vivamus in magna eget erat iaculis iaculis. Cras lacinia, justo ac pellentesque placerat, nunc tortor commodo justo, non cursus leo sem nec metus. Quisque</p>
</section>
<section class="service-panel abs" style="left:650px;top:3800px">
  <h2 class="service-heading abs">About us</h2>
  <p class="panel-text">Lorem ipsum dolor sit amet, consectetur adipiscing elit. Proin tempus dolor vitae purus tincidunt nec iaculis ipsum mollis. Lorem ipsum dolor sit amet, consectetur adipiscing elit. Proin tempus dolor vitae purus tincidunt nec iaculis ipsum mollieret gravida est. Vivamus in magna eget erat iaculis iaculis. Cras lacinia, justo ac pellentesque placerat, nunc tortor commodo justo, non cursus leo sem nec metus. Quisque</p>
</section>

<div class="band featured-title abs">Featured Products</div>

<div class="thumb featured abs" style="left:41px;top:4486px"><div class="thumb-art" role="img" aria-label="Featured product artwork"></div><div class="thumb-ribbon abs">Featured</div></div>
<div class="thumb featured abs" style="left:328px;top:4486px"><div class="thumb-art" role="img" aria-label="Featured product artwork"></div><div class="thumb-ribbon abs">Featured</div></div>
<div class="thumb featured abs" style="left:615px;top:4486px"><div class="thumb-art" role="img" aria-label="Featured product artwork"></div><div class="thumb-ribbon abs">Featured</div></div>
<div class="thumb featured abs" style="left:902px;top:4486px"><div class="thumb-art" role="img" aria-label="Featured product artwork"></div><div class="thumb-ribbon abs">Featured</div></div>

</body>
</html>
```